Torvane Travel Business Card Design

We need a new business card design for our travel agency business - Torvane Travel. We design packages to some of the most popular travel destinations in the world for groups, individuals and also tailor-make personalised packages. Our logo attached must be used. On the back of the card we would like a list of all websites under our Torvane brand to be posted. We would like clean, modern, simple design.

Industry/Entity Type

Travel Agent

Contact Information for Business Card

Owen Pridmore
National Sales Manager
Reservations: 1300 742 689
Tel: 61 28473 5096
Fax: 61 2847 3971
Email: owen@torvanetravel.com.au
Web: www.torvanetravel.com.au

Address: Level 1, 417 Harwick Street
Sydney NSW 2000 Australia

Requirements
Must have
• On the back of the card we want all websites listed under our Torvane brand.
• Torvane Travel Group - Wholesale Specialists
• www.qpjourneys.com.au - New Caledonia
• www.bravelmijourneys.com.au - Tahiti
• www.sorvenbreakhub.com.au - China
Nice to have
• Modern, clean lined, simple and fresh
Should not have
• Look dull

```html
<!DOCTYPE html>
<html lang="en">
<head>
<meta charset="utf-8">
<title>Torvane Travel – Business Card</title>
<link rel="stylesheet" href="https://fonts.googleapis.com/css2?family=Nunito+Sans:wght@400;600;700;800&display=swap">
<style>
  :root {
    --backdrop: #e8ebee;
    --card-white: #f6f6f4;
    --brand-blue: #2d2f8e;
    --name-black: #1f1d1e;
    --ink: #2a2a2a;
    --on-blue: #ffffff;
    --font: "Nunito Sans", Arial, sans-serif;
  }
  * { box-sizing: border-box; margin: 0; padding: 0; }
  html, body {
    width: 1200px; height: 800px; overflow: hidden;
    background: var(--backdrop);
    font-family: var(--font);
  }
  .canvas {
    position: relative; width: 1200px; height: 800px;
    display: flex; align-items: center; justify-content: center; gap: 40px;
  }
  .card {
    position: relative; width: 540px; height: 330px;
    background: var(--card-white); overflow: hidden;
    box-shadow: 0 6px 18px rgba(0,0,0,0.12);
  }

  /* Front (brand side) */
  .front__top-band {
    position: absolute; left: 0; top: 0; width: 100%; height: 24px;
    background: var(--brand-blue);
  }
  .front__brand {
    position: absolute; left: 0; top: 24px; width: 100%; height: 146px;
    display: flex; align-items: center; justify-content: center; gap: 14px;
  }
  .brand-dot {
    width: 22px; height: 22px; border-radius: 50%;
    background: var(--brand-blue);
  }
  .brand-name {
    font-weight: 800; font-size: 50px; letter-spacing: -0.5px;
    color: var(--brand-blue);
  }
  .front__info-band {
    position: absolute; left: 0; top: 170px; width: 100%; height: 128px;
    background: var(--brand-blue); color: var(--on-blue);
    display: flex; flex-direction: column; align-items: center; justify-content: center;
    gap: 4px; text-align: center;
  }
  .front__info-band::before {
    content: ""; position: absolute; left: 50%; top: 0;
    transform: translateX(-50%);
    border-left: 16px solid transparent; border-right: 16px solid transparent;
    border-top: 12px solid var(--card-white);
  }
  .group-name { font-size: 13px; font-weight: 700; letter-spacing: 1px; text-transform: uppercase; margin-bottom: 4px; }
  .site-list { list-style: none; font-size: 12px; line-height: 1.55; }

  /* Back (contact side) */
  .back__name-block {
    position: absolute; right: 0; top: 30px; width: 258px; height: 72px;
    background: var(--name-black); color: var(--on-blue);
    display: flex; flex-direction: column; align-items: center; justify-content: center;
  }
  .person-name { font-size: 17px; font-weight: 800; letter-spacing: 1px; text-transform: uppercase; }
  .person-title { font-size: 13px; font-weight: 400; }
  .back__contacts {
    position: absolute; right: 30px; top: 114px;
    list-style: none; text-align: right;
    font-size: 12.5px; line-height: 17px; color: var(--ink);
  }
  .contact-line { display: flex; justify-content: flex-end; align-items: center; gap: 8px; }
  .contact-line .icon { width: 12px; height: 12px; flex: none; }
  .contact-line .icon--blank { visibility: hidden; }
  .back__stripe {
    position: absolute; left: 0; top: 246px; width: 100%; height: 40px;
    background: var(--brand-blue);
  }
</style>
</head>
<body>
<main class="canvas">

  <section class="card card--front" aria-label="Card front">
    <div class="front__top-band"></div>
    <div class="front__brand">
      <span class="brand-dot"></span>
      <span class="brand-name">Torvane Travel</span>
    </div>
    <div class="front__info-band">
      <p class="group-name">Torvane Travel Group – Wholesale Specialists</p>
      <ul class="site-list">
        <li>www.qpjourneys.com.au – New Caledonia</li>
        <li>www.bravelmijourneys.com.au – Tahiti</li>
        <li>www.sorvenbreakhub.com.au – China</li>
      </ul>
    </div>
  </section>

  <section class="card card--back" aria-label="Card back">
    <div class="back__name-block">
      <p class="person-name">Owen Pridmore</p>
      <p class="person-title">National Sales Manager</p>
    </div>
    <ul class="back__contacts">
      <li class="contact-line">Reservations: 1300 742 689
        <svg class="icon" viewBox="0 0 12 12"><path d="M1 4c0-2 2-3 5-3s5 1 5 3l-2 1-1-1.5H4L3 5zM3 6h6l1 5H2z" fill="#2a2a2a"/></svg>
      </li>
      <li class="contact-line">Tel: 61 28473 5096<svg class="icon icon--blank" viewBox="0 0 12 12"></svg></li>
      <li class="contact-line">Fax: 61 2847 3971
        <svg class="icon" viewBox="0 0 12 12"><rect x="0.5" y="2" width="11" height="8" fill="#2a2a2a"/><path d="M1 2.5l5 4 5-4" stroke="#f6f6f4" stroke-width="1" fill="none"/></svg>
      </li>
      <li class="contact-line">owen@torvanetravel.com.au<svg class="icon icon--blank" viewBox="0 0 12 12"></svg></li>
      <li class="contact-line">www.torvanetravel.com.au
        <svg class="icon" viewBox="0 0 12 12"><g fill="none" stroke="#2a2a2a" stroke-width="1"><circle cx="6" cy="6" r="5"/><ellipse cx="6" cy="6" rx="2.2" ry="5"/><path d="M1 6h10M2 3.5h8M2 8.5h8"/></g></svg>
      </li>
      <li class="contact-line">Level 1, 417 Harwick Street
        <svg class="icon" viewBox="0 0 12 12"><path d="M6 11.5C3 8 2 6 2 4.5a4 4 0 0 1 8 0C10 6 9 8 6 11.5z" fill="#2a2a2a"/><circle cx="6" cy="4.5" r="1.5" fill="#f6f6f4"/></svg>
      </li>
      <li class="contact-line">Sydney NSW 2000 Australia<svg class="icon icon--blank" viewBox="0 0 12 12"></svg></li>
    </ul>
    <div class="back__stripe"></div>
  </section>

</main>
</body>
</html>
```